eCommerce Website Design for Electronic Kits

The company is called Vantrelle. We develop electronic kits, parts & tutorials for hobbyists and engineers. I want something bigger than myself. I can develop and code something, but I want it to be more than I can imagine, so I am here. So, if you feel you have something unique but outside my direction, go for it! I am leaning toward a darker, modern, clean look with a "retro feel," maybe purples, bright reds/pinks, or neon. Our competition is https://www.korbimelt.example and https://www.duvessland.example

Target Market(s)

Hobyists & Engineers (electronics and 3d printing)

Industry/Entity Type

Electronic parts, kits, PCBs, tutorials

Number of Pages Required

4 page

Font styles to use
Sans Serif

Colors

Designer to choose colors to be used in the design.

Requirements
Must have
• Landing / Main Page, Shopping Cart, Item Detail, Blog Post

```html
<!DOCTYPE html>
<html lang="en">
<head>
<meta charset="utf-8">
<title>Vantrelle – Electronic Kits</title>
<link href="https://fonts.googleapis.com/css2?family=Ubuntu:wght@400;500;700&display=swap" rel="stylesheet">
<style>
:root{
  --bg:#000;
  --ink:#fff;
  --pink:#e6047f;
  --pink-line:#d1066f;
  --violet:#3a0f3c;
  --teal-grid:#16343a;
  --muted:#d9d9d9;
  --card-fill:#1a1a1a;
}
*{margin:0;padding:0;box-sizing:border-box}
html,body{width:1200px;height:3567px;overflow:hidden;background:var(--bg)}
body{position:relative;font-family:'Ubuntu',sans-serif;color:var(--ink)}
.abs{position:absolute}
.hero{left:0;top:0;width:1200px;height:680px;
  background:radial-gradient(circle at 600px 290px,#e86bd6 0,#a2249a 90px,transparent 160px),
  linear-gradient(180deg,#0a0630 0,#2a1160 120px,#8a1a8c 300px,#d41f9b 420px,#6c0d5e 520px,#120312 640px,#000 680px)}
.nav{top:62px;left:0;width:1200px;height:20px;font-size:13px;letter-spacing:.2px}
.nav a{position:absolute;color:var(--ink);text-decoration:none;top:0}
.brand{left:540px;top:30px;width:120px;text-align:center;font-size:20px;font-weight:400}
.brand .dot{display:block;width:40px;height:40px;border:2px solid var(--ink);border-radius:50%;margin:0 auto 4px}
.nav svg{position:absolute;top:0}
.welcome{top:246px;width:1200px;text-align:center;font-size:34px;font-weight:500}
.title{top:280px;width:1200px;text-align:center;font-size:112px;font-weight:700;line-height:1}
.btn{position:absolute;background:var(--pink);color:var(--ink);border-radius:4px;text-align:center;font-weight:500;text-decoration:none}
.grid-bg{left:0;width:1200px;background:
  linear-gradient(180deg,#000 0,#160516 30%,#2a0a2a 55%,#120212 85%,#000 100%)}
h2.section{position:absolute;width:1200px;text-align:center;font-size:42px;font-weight:500}
.card{position:absolute;width:236px;height:297px;border:2px solid var(--pink-line);border-radius:6px;background:#000}
.card .ph{position:absolute;left:9px;top:9px;width:214px;height:176px;border-radius:6px}
.card .name{position:absolute;top:202px;width:100%;text-align:center;font-size:15px;font-weight:500}
.card .btn{left:60px;top:240px;width:114px;height:40px;line-height:40px;font-size:15px}
.about-h{left:100px;top:1228px;font-size:42px;font-weight:500}
.about-p{left:100px;top:1296px;width:465px;font-size:13.5px;line-height:30px}
.about-img{left:645px;top:1233px;width:449px;height:372px;border-radius:10px;background:linear-gradient(160deg,#7eb1e0,#5b95cf 60%,#dfe6ee 75%,#cfd6de)}
.ship-h{top:2358px;width:1200px;text-align:center;font-size:33px;font-weight:500}
.ship-p{top:2410px;width:1200px;text-align:center;font-size:16px;line-height:26px}
.cat{position:absolute;top:2699px;width:198px;height:256px;border-radius:99px 99px 0 0;background:var(--card-fill)}
.cat .ph{position:absolute;left:24px;top:28px;width:150px;height:150px;border-radius:20px}
.cat .lbl{position:absolute;top:216px;width:100%;text-align:center;font-size:16px;font-weight:500}
.footer{left:0;top:3000px;width:1200px;height:567px;background:
  radial-gradient(circle at 600px 250px,#5e1660 0,#3a0b3d 120px,transparent 220px),
  linear-gradient(180deg,#000 0,#17071a 20%,#2b0c30 55%,#4a0e46 80%,#1a0418 100%)}
.f-h{position:absolute;font-size:25px;font-weight:500}
.f-h::after{content:"";position:absolute;left:0;top:40px;width:30px;height:2px;background:var(--ink)}
.f-s{position:absolute;font-size:10.5px;line-height:30px}
.f-s.tight{line-height:23px}
.f-logo{left:97px;top:3270px;font-size:40px;font-weight:400}
.f-logo .sq{position:absolute;left:40px;top:-95px;width:80px;height:80px;border:3px solid var(--ink)}
.soc{position:absolute;top:3391px;width:32px;height:32px;border:1.5px solid var(--ink);border-radius:50%}
.email{left:810px;top:3315px;width:276px;height:40px;border-radius:20px;background:#fff;color:#222;font-size:12px;line-height:40px;padding-left:20px}
.email span{position:absolute;right:16px;top:11px;width:18px;height:18px;border-radius:50%;background:#000}
.rule{left:111px;top:3471px;width:978px;height:1px;background:#bbb}
.copy{top:3508px;width:1200px;text-align:center;font-size:14.5px}
</style>
</head>
<body>

<section class="abs hero" role="img" aria-label="Retro synthwave landscape with palm trees, mountains and a glowing sun over a pink horizon"></section>

<nav class="abs nav">
  <a style="left:98px">HOME</a>
  <a style="left:180px">ABOUT US</a>
  <a style="left:283px">OUR PRODUCTS</a>
  <a style="left:422px">TODAY'S DEAL</a>
  <a style="left:688px">SHOP</a>
  <a style="left:763px">LEARN</a>
  <a style="left:845px">BLOG</a>
  <a style="left:918px">SIGN IN</a>
  <svg style="left:1010px" width="15" height="14" viewBox="0 0 15 14" fill="#fff"><path d="M0 1h3l2 7h8l2-6H4" stroke="#fff" stroke-width="1.6" fill="none"/><circle cx="6" cy="12" r="1.5"/><circle cx="12" cy="12" r="1.5"/></svg>
  <svg style="left:1051px" width="15" height="15" viewBox="0 0 15 15"><circle cx="6" cy="6" r="4.5" stroke="#fff" stroke-width="2" fill="none"/><path d="M9.5 9.5L14 14" stroke="#fff" stroke-width="2.4"/></svg>
  <svg style="left:1090px" width="12" height="14" viewBox="0 0 12 14" fill="#fff"><circle cx="6" cy="4" r="3.5"/><path d="M0 14c0-5 12-5 12 0z"/></svg>
</nav>
<div class="abs brand"><span class="dot"></span>Vantrelle</div>

<p class="abs welcome">Welcome to</p>
<h1 class="abs title">Vantrelle</h1>
<a class="btn" style="left:515px;top:410px;width:170px;height:55px;line-height:55px;font-size:20px">Shop Now</a>

<div class="abs grid-bg" style="top:1080px;height:560px" role="img" aria-label="Neon perspective grid backdrop"></div>
<div class="abs grid-bg" style="top:2080px;height:620px" role="img" aria-label="Neon perspective grid backdrop"></div>

<h2 class="section" style="top:705px">New Products</h2>
<div class="card" style="left:100px;top:805px"><div class="ph" role="img" aria-label="Microchip on a circuit trace pattern" style="background:linear-gradient(#fff,#e8eaef)"></div><p class="name">Commodo Consequat</p><a class="btn">Add to Cart</a></div>
<div class="card" style="left:355px;top:805px"><div class="ph" role="img" aria-label="Blue processor chip with connecting traces" style="background:linear-gradient(#fff,#dfe8f5)"></div><p class="name">Reprehenderit</p><a class="btn">Add to Cart</a></div>
<div class="card" style="left:610px;top:805px"><div class="ph" role="img" aria-label="Black USB module" style="background:linear-gradient(#fff,#ececec)"></div><p class="name">Excepteur</p><a class="btn">Add to Cart</a></div>
<div class="card" style="left:864px;top:805px"><div class="ph" role="img" aria-label="Red memory card" style="background:linear-gradient(#fff,#f3e3e3)"></div><p class="name">Cupidatat</p><a class="btn">Add to Cart</a></div>

<h2 class="abs about-h">About Us Vantrelle</h2>
<p class="abs about-p">Sed ut perspiciatis unde omnis iste natus error sit voluptatem accusantium doloremque laudantium, totam rem aperiam, eaque ipsa quae ab illo inventore veritatis et quasi architecto beatae vitae dicta sunt explicabo. Nemo enim ipsam voluptatem quia voluptas sit aspernatur aut odit aut fugit, sed quia consequuntur magni dolores eos qui ratione voluptatem sequi nesciunt. Neque porro quisquam est, qui dolorem ipsum quia dolor sit amet, consectetur, adipisci velit, sed quia non numquam eius modi tempora incidunt ut labore et dolore magnam aliquam quaerat voluptatem.</p>
<a class="btn" style="left:101px;top:1558px;width:114px;height:41px;line-height:41px;font-size:15px">Read More</a>
<div class="abs about-img" role="img" aria-label="Small hobby robot built from parts, wired to a microcontroller board"></div>

<h2 class="section" style="top:1702px">Top Sellers</h2>
<div class="card" style="left:100px;top:1800px"><div class="ph" role="img" aria-label="Black microcontroller board on an edge connector" style="background:linear-gradient(#fff,#e6e6e6)"></div><p class="name">Commodo Consequat</p><a class="btn">Add to Cart</a></div>
<div class="card" style="left:355px;top:1800px"><div class="ph" role="img" aria-label="Black wireless router with four antennas" style="background:linear-gradient(#fff,#ececec)"></div><p class="name">Reprehenderit</p><a class="btn">Add to Cart</a></div>
<div class="card" style="left:610px;top:1800px"><div class="ph" role="img" aria-label="Green and gold processor chip" style="background:linear-gradient(#fff,#eef0dd)"></div><p class="name">Excepteur</p><a class="btn">Add to Cart</a></div>
<div class="card" style="left:864px;top:1800px"><div class="ph" role="img" aria-label="Blue development board" style="background:linear-gradient(#fff,#e1e6f3)"></div><p class="name">Cupidatat</p><a class="btn">Add to Cart</a></div>

<svg class="abs" style="left:538px;top:2258px" width="120" height="62" viewBox="0 0 120 62" fill="#fff">
  <rect x="30" y="6" width="50" height="40" rx="3"/><path d="M82 18h18l14 16v12H82z"/>
  <circle cx="48" cy="50" r="9" stroke="#1b061b" stroke-width="4"/><circle cx="98" cy="50" r="9" stroke="#1b061b" stroke-width="4"/>
  <rect x="4" y="12" width="22" height="3"/><rect x="0" y="22" width="26" height="3"/><rect x="8" y="32" width="18" height="3"/>
</svg>
<h2 class="abs ship-h">FREE SHIPPING* ON ORDERS OVER $200</h2>
<p class="abs ship-p">Duis aute irure dolor in reprehenderit in voluptate velit esse cillum dolore eu fugiat nulla pariatur.<br>Duis aute irure dolor in reprehenderit in voluptate velit esse cillum dolore eu fugiat</p>
<a class="btn" style="left:545px;top:2487px;width:115px;height:42px;line-height:42px;font-size:15px">Orders</a>

<h2 class="section" style="top:2594px">All Categories</h2>
<div class="cat" style="left:125px"><div class="ph" role="img" aria-label="Neon pink chip gear icon" style="background:radial-gradient(#c13ad6,#3a1240 70%,transparent)"></div><p class="lbl">Engineering Essentials</p></div>
<div class="cat" style="left:375px"><div class="ph" role="img" aria-label="Neon blue map pin icon" style="background:radial-gradient(#2c7ef0,#122a4d 70%,transparent)"></div><p class="lbl">Building a GPS System</p></div>
<div class="cat" style="left:625px"><div class="ph" role="img" aria-label="Neon pink card reader icon" style="background:radial-gradient(#c13ad6,#3a1240 70%,transparent)"></div><p class="lbl">RFID Tags and Readers</p></div>
<div class="cat" style="left:875px"><div class="ph" role="img" aria-label="Neon blue wireless router icon" style="background:radial-gradient(#2c7ef0,#122a4d 70%,transparent)"></div><p class="lbl">Working with WiFi</p></div>

<footer class="abs footer" role="img" aria-label="Dim synthwave palm tree skyline"></footer>
<div class="abs f-logo"><span class="sq"></span>Vantrelle</div>
<span class="soc" style="left:100px"></span><span class="soc" style="left:138px"></span>

<h3 class="f-h" style="left:363px;top:3188px">More Info</h3>
<p class="f-s" style="left:363px;top:3245px">Terms &amp; Conditions<br>Privacy Policy<br>About Us<br>Support</p>

<h3 class="f-h" style="left:561px;top:3186px">Contact Us</h3>
<p class="f-s tight" style="left:561px;top:3244px">ADDRESS<br>⌖ Lorem ipsum dolor sit amet,<br>consectetura 25516</p>
<p class="f-s" style="left:561px;top:3323px">PHONE<br>✆ +1 888-888-88888</p>
<p class="f-s" style="left:561px;top:3385px">EMAIL<br>✉ info@vantrelle.example</p>

<h3 class="f-h" style="left:812px;top:3186px">Newsletter</h3>
<p class="f-s tight" style="left:812px;top:3244px">Lorem ipsum dolor sit amet, consectetur<br>adipiscing elit, sed do eiusmod tempor</p>
<div class="abs email">Enter Email<span></span></div>

<div class="abs rule"></div>
<p class="abs copy">© copyrights 2024 Vantrelle &nbsp;|&nbsp; All Rights Reserved</p>

</body>
</html>
```